Loan Application Project

We have a bank application form in pdf and we wish to use the content of the application to develop a loan application using our own brand and look / feel with the brand of a Partner.

The content of the application can be simply copied across. We assume that the process for doing this is easy when armed with the right pdf software.
Updates

Hi - I have now added both the second logo that needs incorporating and also gone through and made changes to the text on the actual application form so this project is now ready to "bring home".  Thanks Gordon

Target Market(s)

Samll Business Operators

Industry/Entity Type

Bank

Requirements
Must have
• Must remove all reference to Coastal Meridian Bank or CMB and replace with Tallow Credit Services Pty Ltd (Tallow). I'd be happy to go through the hard copy and scan a copy where I have hand written changes for the designer
Nice to have
• To be able to electronically complete the form would be great. Not sure how you do this but I know it can be done for pdf forms.

```html
<!DOCTYPE html>
<html lang="en">
<head>
<meta charset="utf-8">
<title>Monthly Budget – Individuals</title>
<link rel="stylesheet" href="https://fonts.googleapis.com/css2?family=Istok+Web:wght@400;700&display=swap">
<style>
:root{
  --ink:#1c1c1c;
  --panel:#e5efee;
  --field:#ffffff;
  --rule:#5a5a5a;
  --page:#ffffff;
}
*{box-sizing:border-box;margin:0;padding:0}
html,body{width:849px;height:1200px;overflow:hidden;background:var(--page)}
body{font-family:"Istok Web",Arial,sans-serif;color:var(--ink);font-size:9.5px;line-height:1.25}
.sheet{position:relative;width:849px;height:1200px}
.top-band{position:absolute;left:40px;top:40px;width:769px;height:17px;background:var(--ink)}
.panel{position:absolute;left:40px;top:57px;width:769px;height:1103px;background:var(--panel)}
.title-rule{position:absolute;left:74px;top:69px;width:726px;border-top:1px solid var(--rule)}
.title-mark{position:absolute;left:52px;top:70px;width:22px;height:15px;background:var(--ink)}
.title{position:absolute;left:82px;top:70px;font-size:13.5px;font-weight:700}
.title small{font-size:9px}
.t{position:absolute;white-space:nowrap}
.b{font-weight:700}
.r{text-align:right}
.field{position:absolute;height:21px;width:98px;background:var(--field);border-left:1px solid var(--rule);border-bottom:1px solid var(--rule);padding:4px 0 0 6px;font-size:10px}
.field.wide{width:155px}
.field.desc{width:154px}
.field.total{border:2px solid var(--ink);font-weight:700}
.notes{position:absolute;left:51px;top:494px;width:364px;height:62px;background:var(--field);border-left:1px solid var(--rule);border-bottom:1px solid var(--rule)}
.notes i{position:absolute;left:4px;right:0;border-top:1px solid var(--rule)}
.folio{position:absolute;right:41px;top:1163px;font-size:8.5px}
</style>
</head>
<body>
<main class="sheet">
  <div class="top-band"></div>
  <section class="panel"></section>
  <div class="title-rule"></div>
  <div class="title-mark"></div>
  <h1 class="title">Monthly Budget – Individuals <small>(use annual amounts divided by 12)</small></h1>

  <!-- Monthly income -->
  <span class="t b" style="left:51px;top:100px">Monthly Income</span>
  <span class="t" style="left:213px;top:112px">Gross salary</span>
  <span class="t" style="left:318px;top:112px">After tax salary</span>
  <span class="t r" style="left:51px;top:132px;width:137px">*Salary (attach salary slip)</span>
  <div class="field" style="left:212px;top:126px">$</div>
  <div class="field" style="left:317px;top:126px">$</div>
  <span class="t" style="left:51px;top:153px;white-space:normal;width:370px">*Other income (Study assistance payment, Family Allowance, Part-time work, Dividends, Interest etc) – attach evidence</span>
  <span class="t" style="left:51px;top:184px">Description</span>
  <span class="t" style="left:213px;top:184px">Gross income</span>
  <span class="t" style="left:318px;top:184px">After tax income</span>

  <div class="field desc" style="left:51px;top:199px"></div><div class="field" style="left:212px;top:199px">$</div><div class="field" style="left:317px;top:199px">$</div>
  <div class="field desc" style="left:51px;top:227px"></div><div class="field" style="left:212px;top:227px">$</div><div class="field" style="left:317px;top:227px">$</div>
  <div class="field desc" style="left:51px;top:255px"></div><div class="field" style="left:212px;top:255px">$</div><div class="field" style="left:317px;top:255px">$</div>
  <div class="field desc" style="left:51px;top:283px"></div><div class="field" style="left:212px;top:283px">$</div><div class="field" style="left:317px;top:283px">$</div>
  <div class="field desc" style="left:51px;top:311px"></div><div class="field" style="left:212px;top:311px">$</div><div class="field" style="left:317px;top:311px">$</div>

  <span class="t" style="left:213px;top:338px">Gross</span>
  <span class="t" style="left:318px;top:338px">After expenses</span>
  <span class="t r" style="left:51px;top:357px;width:137px">*Rental income</span>
  <div class="field" style="left:212px;top:352px">$</div><div class="field" style="left:317px;top:352px">$</div>
  <span class="t" style="left:213px;top:378px">Net profit</span>
  <span class="t" style="left:318px;top:378px">After tax profit</span>
  <span class="t r" style="left:51px;top:397px;width:137px">*Self-employed entities</span>
  <div class="field" style="left:212px;top:392px">$</div><div class="field" style="left:317px;top:392px">$</div>
  <span class="t b r" style="left:100px;top:425px;width:193px">Total net income per month</span>
  <div class="field total" style="left:317px;top:419px">$</div>

  <span class="t" style="left:51px;top:460px"><b>*Employment Package</b> – do not add into total income</span>
  <div class="field" style="left:317px;top:455px">$</div>
  <span class="t" style="left:51px;top:480px">Package includes (eg. salary, car etc)</span>
  <div class="notes"><i style="top:20px"></i><i style="top:41px"></i></div>
  <span class="t" style="left:51px;top:561px;white-space:normal;width:345px"><b>*Note:</b> Please produce evidence of income, for example, two (2) recent payslips, or for self-employed entity, copies of the last (3) years' financial statements.</span>

  <!-- Budget summary -->
  <span class="t b" style="left:51px;top:924px">Budget Summary</span>
  <span class="t" style="left:213px;top:935px">Pre loan</span>
  <span class="t" style="left:318px;top:935px">Post loan</span>
  <span class="t b r" style="left:51px;top:955px;width:137px">Total net income per month</span>
  <div class="field" style="left:212px;top:950px">$</div><div class="field" style="left:317px;top:950px">$</div>
  <span class="t" style="left:51px;top:976px">Deduct</span>
  <span class="t b r" style="left:51px;top:995px;width:137px">Total monthly payments</span>
  <div class="field" style="left:212px;top:990px">$</div><div class="field" style="left:317px;top:990px">$</div>
  <span class="t b r" style="left:51px;top:1022px;width:137px">Total usable funds</span>
  <div class="field total" style="left:212px;top:1017px">$</div><div class="field total" style="left:317px;top:1017px">$</div>

  <!-- Monthly expenditure -->
  <span class="t b" style="left:434px;top:100px">Monthly Expenditure</span>
  <span class="t" style="left:434px;top:121px">Home Loans</span>
  <span class="t" style="left:597px;top:121px">Pre Loan</span>
  <span class="t" style="left:702px;top:121px">Post Loan</span>
  <div class="field wide" style="left:434px;top:134px">1.</div><div class="field" style="left:597px;top:134px">$</div><div class="field" style="left:702px;top:134px">$</div>
  <div class="field wide" style="left:434px;top:162px">2.</div><div class="field" style="left:597px;top:162px">$</div><div class="field" style="left:702px;top:162px">$</div>
  <div class="field wide" style="left:434px;top:190px">3.</div><div class="field" style="left:597px;top:190px">$</div><div class="field" style="left:702px;top:190px">$</div>
  <span class="t r" style="left:434px;top:225px;width:139px">Personal Loan</span>
  <div class="field" style="left:597px;top:219px">$</div><div class="field" style="left:702px;top:219px">$</div>
  <span class="t" style="left:434px;top:249px">Other Loans (Finance co., Other bank etc.)</span>
  <div class="field wide" style="left:434px;top:263px">1.</div><div class="field" style="left:597px;top:263px">$</div><div class="field" style="left:702px;top:263px">$</div>
  <div class="field wide" style="left:434px;top:291px">2.</div><div class="field" style="left:597px;top:291px">$</div><div class="field" style="left:702px;top:291px">$</div>
  <span class="t" style="left:434px;top:321px">Credit/Store Cards</span>
  <div class="field wide" style="left:434px;top:336px">1.</div><div class="field" style="left:597px;top:336px">$</div><div class="field" style="left:702px;top:336px">$</div>
  <div class="field wide" style="left:434px;top:364px">2.</div><div class="field" style="left:597px;top:364px">$</div><div class="field" style="left:702px;top:364px">$</div>
  <span class="t" style="left:434px;top:394px">Other Debts (give details)</span>
  <div class="field wide" style="left:434px;top:408px">1.</div><div class="field" style="left:597px;top:408px">$</div><div class="field" style="left:702px;top:408px">$</div>
  <div class="field wide" style="left:434px;top:436px">2.</div><div class="field" style="left:597px;top:436px">$</div><div class="field" style="left:702px;top:436px">$</div>
  <span class="t b r" style="left:434px;top:469px;width:139px">Total loan repayments</span>
  <div class="field total" style="left:597px;top:463px">$</div><div class="field" style="left:702px;top:463px">$</div>

  <span class="t" style="left:597px;top:494px">Pre loan</span>
  <span class="t" style="left:702px;top:494px">Post Loan</span>

  <span class="t" style="left:443px;top:513px">Rent</span>
  <div class="field" style="left:597px;top:508px">$</div><div class="field" style="left:702px;top:508px">$</div>
  <span class="t" style="left:443px;top:541px">Insurance</span><span class="t" style="left:503px;top:541px">– Health</span>
  <div class="field" style="left:597px;top:536px">$</div><div class="field" style="left:702px;top:536px">$</div>
  <span class="t" style="left:503px;top:569px">– Home</span>
  <div class="field" style="left:597px;top:564px">$</div><div class="field" style="left:702px;top:564px">$</div>
  <span class="t" style="left:503px;top:597px">– Car</span>
  <div class="field" style="left:597px;top:592px">$</div><div class="field" style="left:702px;top:592px">$</div>
  <span class="t" style="left:503px;top:625px">– Life</span>
  <div class="field" style="left:597px;top:620px">$</div><div class="field" style="left:702px;top:620px">$</div>
  <span class="t" style="left:503px;top:648px;line-height:1.1">– Income<br>&nbsp;&nbsp;&nbsp;Protection</span>
  <div class="field" style="left:597px;top:648px">$</div><div class="field" style="left:702px;top:648px">$</div>
  <span class="t" style="left:443px;top:682px">School fees</span>
  <div class="field" style="left:597px;top:677px">$</div><div class="field" style="left:702px;top:677px">$</div>
  <span class="t" style="left:443px;top:710px">Electricity</span>
  <div class="field" style="left:597px;top:705px">$</div><div class="field" style="left:702px;top:705px">$</div>
  <span class="t" style="left:443px;top:738px">Gas</span>
  <div class="field" style="left:597px;top:733px">$</div><div class="field" style="left:702px;top:733px">$</div>
  <span class="t" style="left:443px;top:767px">Telephone</span>
  <div class="field" style="left:597px;top:762px">$</div><div class="field" style="left:702px;top:762px">$</div>
  <span class="t" style="left:443px;top:795px">Medical expenses</span>
  <div class="field" style="left:597px;top:790px">$</div><div class="field" style="left:702px;top:790px">$</div>
  <span class="t" style="left:443px;top:823px">Rates (Council/Water)</span>
  <div class="field" style="left:597px;top:818px">$</div><div class="field" style="left:702px;top:818px">$</div>
  <span class="t" style="left:443px;top:852px">Car/Travel</span>
  <div class="field" style="left:597px;top:847px">$</div><div class="field" style="left:702px;top:847px">$</div>
  <span class="t" style="left:443px;top:880px">Food</span>
  <div class="field" style="left:597px;top:875px">$</div><div class="field" style="left:702px;top:875px">$</div>
  <span class="t" style="left:443px;top:908px">Clothing</span>
  <div class="field" style="left:597px;top:903px">$</div><div class="field" style="left:702px;top:903px">$</div>
  <span class="t" style="left:443px;top:937px">Entertainment</span>
  <div class="field" style="left:597px;top:932px">$</div><div class="field" style="left:702px;top:932px">$</div>
  <span class="t" style="left:443px;top:965px">Subscription</span>
  <div class="field" style="left:597px;top:960px">$</div><div class="field" style="left:702px;top:960px">$</div>
  <span class="t" style="left:443px;top:993px;font-size:9px">Others (Superannuation, Gifts etc)</span>
  <div class="field" style="left:597px;top:988px">$</div><div class="field" style="left:702px;top:988px">$</div>
  <span class="t b r" style="left:434px;top:1022px;width:139px">Total monthly payments</span>
  <div class="field total" style="left:597px;top:1017px">$</div><div class="field total" style="left:702px;top:1017px">$</div>

  <footer class="folio">Page 11 of 14</footer>
</main>
</body>
</html>
```